Tri-fold flyer for Managed Services IT company

We need a tri-fold flyer design for our Managed Services IT company. Our website is here: https://pelicanfjordit.net. While we don't have to match our website we do want to incorporate the logo in the flyer. We would like a flyer that is *very* easy and quick to read/skim over and convey our message. Something like these:

https://www.artkestrel.com/design/58203917

https://47sketchyard.com/postcard-flyer-design/contests/create-lead-generating-flyer-postcard-managed-services-company-815243

http://www.marbleoaksystems.com/managed-services-no-cost-one-month/

Target Market(s)

Business to business IT services

Industry/Entity Type

It Service

Font styles to use
Serif
Sans Serif

Requirements
Must have
• *very* easy and quick to read/skim over and convey our message
Should not have
• verbose, lots of text

```html
<!DOCTYPE html>
<html lang="en">
<head>
<meta charset="utf-8">
<title>Pelican Fjord – Tri-fold Flyer</title>
<link rel="stylesheet" href="https://fonts.googleapis.com/css2?family=Cinzel:wght@600;700&family=Open+Sans:wght@400;600;700;800&display=swap">
<style>
:root{
  --navy:#132d6b;
  --navy-deep:#0b1b45;
  --blue:#1f4aa8;
  --orange:#f27a1a;
  --orange-dark:#d9620b;
  --white:#ffffff;
  --ink:#2a2f3a;
  --paper:#eef0f4;
}
*{margin:0;padding:0;box-sizing:border-box}
html,body{width:1200px;height:2568px;overflow:hidden}
body{background:var(--paper);font-family:"Open Sans",Arial,sans-serif;color:var(--ink);position:relative}
.spread{position:absolute;left:20px;width:1160px;height:780px;display:grid;grid-template-columns:repeat(3,1fr);box-shadow:0 6px 24px rgba(0,0,0,.18);overflow:hidden}
.spread.outside{top:474px}
.spread.inside{top:1314px;background:linear-gradient(180deg,var(--navy-deep) 0%,var(--navy) 55%,var(--blue) 100%);grid-template-rows:110px 1fr;column-gap:0}
.panel{position:relative;overflow:hidden}

/* outside – about panel */
.about{background:var(--white);display:flex;flex-direction:column}
.about .photo-office{height:220px;background:linear-gradient(135deg,#c9d6ea,#8fa6c9 60%,#5b77a8)}
.about .rule{height:8px;background:var(--orange)}
.about .copy{padding:22px 26px 0;font-size:12.5px;line-height:1.55;color:#3a3f4a}
.about .copy p+p{margin-top:12px}
.about .photo-team{margin:18px 26px 0;height:120px;background:linear-gradient(180deg,#dfe5ee,#aab6c9)}
.about .url{position:absolute;bottom:22px;left:26px;font-weight:800;color:var(--navy);font-size:14px}

/* outside – contact panel */
.contact{background:linear-gradient(180deg,var(--blue),var(--navy) 70%,var(--navy-deep));color:var(--white);text-align:center}
.ribbon{margin:46px auto 0;width:240px;height:46px;background:var(--orange);line-height:46px;font-weight:700;font-size:22px;position:relative}
.phone{margin-top:18px;font-weight:800;font-size:46px;letter-spacing:.5px}
.contact svg.wave{position:absolute;left:0;top:210px}
.brand{display:flex;align-items:center;justify-content:center;gap:10px;font-family:"Open Sans",Arial,sans-serif;font-weight:700;letter-spacing:3px}
.contact .brand{position:absolute;top:340px;left:0;right:0;font-size:24px;color:var(--white)}
.brand .dot{width:16px;height:16px;border-radius:50%;background:var(--orange)}
.address{position:absolute;top:560px;left:0;right:0;font-weight:700;font-size:16px;line-height:1.45}
.contact .url{position:absolute;bottom:26px;left:0;right:0;font-weight:700;font-size:14px}

/* outside – cover panel */
.cover{background:var(--navy)}
.cover .head{height:220px;background:var(--white);display:flex;align-items:center;justify-content:center}
.cover .brand{font-size:24px;color:var(--navy)}
.cover .photo-tablet{position:absolute;top:220px;left:0;right:0;height:330px;background:linear-gradient(160deg,#2f63c2,#153a86 55%,#0c2258)}
.cover svg.swoosh{position:absolute;top:180px;left:0}
.cover .tag{position:absolute;top:590px;left:0;right:0;text-align:center;color:var(--white)}
.cover .tag .small{font-family:"Cinzel",Georgia,serif;font-size:26px;color:var(--orange)}
.cover .tag .big{font-family:"Cinzel",Georgia,serif;font-size:30px;font-weight:700;margin-top:4px}
.cover .url{position:absolute;bottom:26px;left:0;right:0;text-align:center;color:var(--white);font-weight:700;font-size:14px}

/* inside */
.title{grid-column:1/4;display:flex;align-items:center;justify-content:center;font-family:"Cinzel",Georgia,serif;font-weight:600;font-size:40px;letter-spacing:14px;color:var(--white)}
.service{padding:0 26px;color:var(--white);position:relative}
.service h2{background:var(--orange);font-size:20px;font-weight:700;text-align:center;padding:9px 0}
.icons{display:flex;justify-content:center;gap:18px;margin:16px 0 14px}
.icon{width:40px;height:40px;border-radius:50%;border:2px solid var(--orange);display:flex;align-items:center;justify-content:center}
.service p{font-size:11.5px;line-height:1.5;opacity:.92}
.service ul{list-style:none;margin-top:16px}
.service li{font-size:12.5px;font-weight:600;line-height:1.3;padding:5px 0 5px 18px;position:relative}
.service li::before{content:"";position:absolute;left:0;top:9px;border-left:8px solid var(--orange);border-top:5px solid transparent;border-bottom:5px solid transparent}
.skyline{position:absolute;left:0;right:0;bottom:0;height:90px;background:linear-gradient(180deg,rgba(31,74,168,0),rgba(110,150,210,.35))}
</style>
</head>
<body>

<section class="spread outside">
  <div class="panel about">
    <div class="photo-office" role="img" aria-label="Photo of business team working together at an office table"></div>
    <div class="rule"></div>
    <div class="copy">
      <p>Pelican Fjord has been serving the Bethesda area since 2006, providing IT support such as technical helpdesk support, computer support, and consulting to small and mid-sized businesses. It's always been our goal to provide professional IT practices and solutions to help the growth of our client's businesses. Our experience has allowed us to build and maintain the infrastructure needed to keep you safe, affordable and your clients up and running.</p>
      <p>We partner with many types of businesses in the area, and we're a reliable IT team before they notice expensive downtime, so you can continue to drive your business forward. Our dedicated staff love seeing our clients succeed. Your success is our success, and we grow together.</p>
    </div>
    <div class="photo-team" role="img" aria-label="Photo of the support staff group"></div>
    <div class="url">https://pelicanfjordit.net</div>
  </div>

  <div class="panel contact">
    <div class="ribbon">Call Us Today</div>
    <div class="phone">301-555-0184</div>
    <svg class="wave" width="387" height="80" viewBox="0 0 387 80"><path d="M0 60 C120 10 260 10 387 40 L387 52 C260 24 120 26 0 74 Z" fill="#ffffff"/><path d="M0 74 C130 30 260 34 387 52" stroke="#f27a1a" stroke-width="4" fill="none"/></svg>
    <div class="brand"><span class="dot"></span>PELICAN FJORD</div>
    <div class="address">4810 Harbor Crest Road 3B<br>Bethesda, Maryland 20814</div>
    <div class="url">https://pelicanfjordit.net</div>
  </div>

  <div class="panel cover">
    <div class="head"><div class="brand"><span class="dot"></span>PELICAN FJORD</div></div>
    <div class="photo-tablet" role="img" aria-label="Photo of a hand holding a tablet in blue light"></div>
    <svg class="swoosh" width="387" height="120" viewBox="0 0 387 120"><path d="M0 40 C140 100 280 80 387 10 L387 40 C280 100 140 120 0 70 Z" fill="#ffffff"/><path d="M0 70 C140 118 280 100 387 40 L387 56 C280 112 140 130 0 86 Z" fill="#f27a1a"/></svg>
    <div class="tag"><div class="small">The DC Metro</div><div class="big">IT Support Experts</div></div>
    <div class="url">https://pelicanfjordit.net</div>
  </div>
</section>

<section class="spread inside">
  <div class="title">SOME OF OUR SERVICES</div>

  <div class="service">
    <h2>Managed IT Services</h2>
    <div class="icons">
      <span class="icon"><svg width="20" height="20" viewBox="0 0 20 20"><rect x="2" y="3" width="16" height="11" fill="none" stroke="#fff" stroke-width="2"/><path d="M6 17h8" stroke="#fff" stroke-width="2"/></svg></span>
      <span class="icon"><svg width="20" height="20" viewBox="0 0 20 20"><path d="M4 10l4 4 8-9" fill="none" stroke="#fff" stroke-width="2.4"/></svg></span>
      <span class="icon"><svg width="20" height="20" viewBox="0 0 20 20"><circle cx="10" cy="10" r="6" fill="none" stroke="#fff" stroke-width="2"/><path d="M10 6v4l3 2" stroke="#fff" stroke-width="2" fill="none"/></svg></span>
    </div>
    <p>Do you depend on technology to maximize the efficiency of your team? Our managed service plans put you ahead of issues, keep costs predictable and free your staff to focus on growth. We monitor, patch and support every device so problems are solved before you notice them.</p>
    <ul>
      <li>Pelican Fjord IT Consulting Services</li>
      <li>IT Support – Helpdesk Services</li>
      <li>Remote Monitoring and Maintenance – A Cost Effective Solution to Proactive Management</li>
      <li>IT Vendor Management – Virtual CIO</li>
      <li>VoIP Management</li>
      <li>Vertex Virtualization Solutions</li>
      <li>24/7 Help Desk</li>
      <li>Norvane Project Services</li>
      <li>Upgrade Legacy Servers to Current Platforms</li>
      <li>Manage desktop computers with ease</li>
    </ul>
    <div class="skyline" role="img" aria-label="Faint city skyline at dusk"></div>
  </div>

  <div class="service">
    <h2>Cloud IT Services</h2>
    <div class="icons">
      <span class="icon"><svg width="22" height="20" viewBox="0 0 22 20"><path d="M6 15h11a4 4 0 0 0 0-8 6 6 0 0 0-11 1 3.5 3.5 0 0 0 0 7z" fill="none" stroke="#fff" stroke-width="2"/></svg></span>
      <span class="icon"><svg width="20" height="20" viewBox="0 0 20 20"><rect x="3" y="3" width="14" height="5" fill="none" stroke="#fff" stroke-width="2"/><rect x="3" y="12" width="14" height="5" fill="none" stroke="#fff" stroke-width="2"/></svg></span>
      <span class="icon"><svg width="20" height="20" viewBox="0 0 20 20"><path d="M10 3v11M5 9l5 5 5-5" fill="none" stroke="#fff" stroke-width="2"/></svg></span>
    </div>
    <p>Companies are starting to utilize cloud computing to improve performance. We move your files, email and apps to secure hosted platforms so your team works from anywhere, scales on demand and keeps data backed up and protected around the clock.</p>
    <ul>
      <li>Hosted Email Exchange</li>
      <li>Hosted Server Solutions</li>
      <li>Virtualized Desktop Solutions from Pelican Fjord</li>
      <li>Hardware Virtualization</li>
      <li>Cloud Backup, Security, and File Sharing Protection</li>
      <li>Simplified Access to the Cloud</li>
      <li>Boxhaven Storage for Business</li>
      <li>Cut Cloud Computing Platform &amp; Infrastructure Costs</li>
      <li>Cloud Based VoIP</li>
    </ul>
    <div class="skyline" role="img" aria-label="Faint city skyline at dusk"></div>
  </div>

  <div class="service">
    <h2>Security Services</h2>
    <div class="icons">
      <span class="icon"><svg width="20" height="20" viewBox="0 0 20 20"><path d="M10 2l7 3v5c0 4-3 7-7 8-4-1-7-4-7-8V5z" fill="none" stroke="#fff" stroke-width="2"/></svg></span>
      <span class="icon"><svg width="20" height="20" viewBox="0 0 20 20"><rect x="4" y="9" width="12" height="9" fill="none" stroke="#fff" stroke-width="2"/><path d="M7 9V6a3 3 0 0 1 6 0v3" fill="none" stroke="#fff" stroke-width="2"/></svg></span>
      <span class="icon"><svg width="20" height="20" viewBox="0 0 20 20"><circle cx="9" cy="9" r="5" fill="none" stroke="#fff" stroke-width="2"/><path d="M13 13l4 4" stroke="#fff" stroke-width="2"/></svg></span>
    </div>
    <p>Standard, point-in-time security checks are highly difficult to handle. Our layered approach to security protects your network, devices and data with firewalls, filtering and endpoint tools, managed from one place.</p>
    <ul>
      <li>Unified Threat Management</li>
      <li>Web Filtering &amp; Firewall</li>
      <li>Spam Protection</li>
      <li>Digital Security Camera Systems</li>
      <li>Shieldra Security Solutions</li>
      <li>Powerful next-gen endpoint protection for you, your clients, and your network</li>
      <li>Corvalen Certified Solutions</li>
      <li>Fully Vetted Security as a Service – leverage the Cloud to Protect Your Network</li>
    </ul>
    <div class="skyline" role="img" aria-label="Faint city skyline at dusk"></div>
  </div>
</section>

</body>
</html>
```